Australian small vineyard seeking wine label.

We need a wine label design for a new wine brand \Boutique winery - 2 vintages so far, looking for something a little eye catching, but simple.
Wine label name: Brent and Co
2013 Cabernet Shiraz
2014 Shiraz
Estate grown
Vineyard located at Sevenhill in the Clare valley South Australia.

Target Market(s)

ladies aged between 20 and 50

Industry/Entity Type

Boutique

Logo Text

Brent and Co

Logo styles of interest
Emblem Logo
Pictorial/Combination Logo
Abstract Logo
Character Logo
Font styles to use
Serif
Script

Requirements
Must have
• easy to read text
Nice to have
• The grape grower and winemaker is Martin Brent -
• had some thoughts of Captain Brent - Australian - naval flag
• But very open to ideas
Should not have
• over complications and colors due to cost of wine label being determined by amount of colors required abd print set up.

```html
<!DOCTYPE html>
<html lang="en">
<head>
<meta charset="utf-8">
<title>Brent and Co — 2013 Cabernet Shiraz Label</title>
<link rel="stylesheet" href="https://fonts.googleapis.com/css2?family=Libre+Baskerville:wght@400&display=swap">
<style>
  :root {
    --page-bg: #ffffff;
    --label-cream: #efebd0;
    --label-edge: #e2dcbd;
    --wine-red: #c41e35;
    --ink: #2b2323;
    --rule-grey: #b5b0a0;
    --art-light: #d9d5c2;
    --art-dark: #3a3636;
  }
  * { margin: 0; padding: 0; box-sizing: border-box; }
  html, body {
    width: 1200px;
    height: 1000px;
    overflow: hidden;
    background: var(--page-bg);
  }
  .canvas {
    position: relative;
    width: 1200px;
    height: 1000px;
  }
  .label {
    position: absolute;
    left: 370px;
    top: 80px;
    width: 460px;
    height: 840px;
    background: var(--label-cream);
    border: 1px solid var(--label-edge);
    border-radius: 0 0 50% 50% / 0 0 22px 22px;
    font-family: "Libre Baskerville", Georgia, serif;
    font-weight: 400;
    text-align: center;
  }
  .label > * {
    position: absolute;
    left: 0;
    width: 100%;
    font-weight: 400;
  }
  .brand-name {
    top: 52px;
    font-size: 50px;
    line-height: 1;
    color: var(--wine-red);
  }
  .portrait-medallion {
    top: 120px;
    left: 100px;
    width: 260px;
    height: 260px;
  }
  .vine-band {
    top: 385px;
    left: 30px;
    width: 400px;
    height: 70px;
  }
  .vintage {
    top: 474px;
    font-size: 36px;
    line-height: 1;
    color: var(--wine-red);
  }
  .estate {
    top: 522px;
    font-size: 19px;
    line-height: 1;
    color: var(--wine-red);
  }
  .varietal {
    top: 582px;
    font-size: 44px;
    line-height: 1;
    color: var(--wine-red);
  }
  .divider {
    top: 646px;
    left: 25px;
    width: 410px;
    height: 3px;
    background: var(--rule-grey);
  }
  .region {
    top: 682px;
    font-size: 21px;
    line-height: 1;
    color: var(--ink);
  }
  .origin {
    top: 736px;
    font-size: 29px;
    line-height: 1;
    color: var(--ink);
  }
</style>
</head>
<body>
<main class="canvas">
  <section class="label">
    <h1 class="brand-name">Brent and Co</h1>

    <svg class="portrait-medallion" viewBox="0 0 266 266" role="img" aria-label="Engraved portrait of Captain Brent in a round frame">
      <defs>
        <radialGradient id="medallion-tone" cx="50%" cy="45%" r="55%">
          <stop offset="0%" stop-color="#d9d5c2"/>
          <stop offset="100%" stop-color="#3a3636"/>
        </radialGradient>
      </defs>
      <circle cx="133" cy="133" r="130" fill="none" stroke="#b5b0a0" stroke-width="4"/>
      <circle cx="133" cy="133" r="118" fill="url(#medallion-tone)"/>
    </svg>

    <svg class="vine-band" viewBox="0 0 400 70" role="img" aria-label="Ornamental grapevine with leaves and grape clusters">
      <defs>
        <linearGradient id="vine-tone" x1="0" x2="1" y1="0" y2="0">
          <stop offset="0%" stop-color="#3a3636" stop-opacity="0.15"/>
          <stop offset="50%" stop-color="#3a3636" stop-opacity="0.85"/>
          <stop offset="100%" stop-color="#3a3636" stop-opacity="0.15"/>
        </linearGradient>
      </defs>
      <rect x="0" y="10" width="400" height="50" rx="25" fill="url(#vine-tone)"/>
    </svg>

    <p class="vintage">2013</p>
    <p class="estate">Estate grown</p>
    <h2 class="varietal">Cabernet Shiraz</h2>
    <div class="divider"></div>
    <p class="region">Sevenhill • Clare valley</p>
    <p class="origin">Wine of South Australia</p>
  </section>
</main>
</body>
</html>
```